Unique and original Business Card for Financial Services Business

I have moved premises and need to change the detail on my business card so thought now is a good time for a re-design. Looking for something professional and modern with colours to fit in with out logo. Like the idea of foil or embossing if that works but not a must have but I do want something that stands out and that I could not design myself.

Once business card is designed I will also be looking to get letterhead and flyers done but want the business card concept in place first.

The majority of designs I am receiving are generic and template based. I am looking for something unique and original. We have some great design elements in our logo, think outside the box and show me something that stands out from the crowd.

Target Market(s)

Business Professionals

Industry/Entity Type

Finance

Contact Information for Business Card

Name: Delia Norwood Phone 0473 958 162 Address PO Box 8617 Mossvale NSW 2389 Email info@steadyharbourfinancialservices.com.au website www.steadyharbourfinancialservices.com.au

Font styles to use
Other font styles liked:
• Ralway

Requirements
Should not have
• No black backgrounds please

```html
<!DOCTYPE html>
<html lang="en">
<head>
<meta charset="utf-8">
<title>Steady Harbour Financial Services – Business Card</title>
<link rel="stylesheet" href="https://fonts.googleapis.com/css2?family=Urbanist:wght@400;500;600;800&display=swap">
<style>
  :root {
    --backdrop: #8e8e8e;
    --card-white: #eaeaec;
    --ink: #1d1d1f;
    --teal-dark: #0f6072;
    --teal-card: #007d8e;
    --teal-raised: #0aa0b2;
  }
  * { margin: 0; padding: 0; box-sizing: border-box; }
  html, body {
    width: 1200px; height: 1200px; overflow: hidden;
    background: var(--backdrop);
    font-family: "Urbanist", sans-serif;
  }
  .canvas { position: relative; width: 1200px; height: 1200px; }

  .card {
    position: absolute; left: 225px; width: 750px; height: 416px;
  }
  .card--front { top: 101px; background: var(--card-white); }
  .card--back { top: 667px; background: var(--teal-card); }

  .holder { position: absolute; left: 60px; top: 40px; }
  .holder__name {
    font-weight: 800; font-size: 27px; color: var(--teal-dark); line-height: 1.1;
  }
  .holder__role {
    font-weight: 400; font-size: 19px; color: var(--ink); margin-top: 2px;
  }

  .contact-list {
    position: absolute; left: 60px; top: 118px; list-style: none;
  }
  .contact-list__item {
    display: flex; align-items: center; height: 29px;
    font-size: 19px; font-weight: 400; color: var(--ink); letter-spacing: 0.1px;
  }
  .contact-list__icon { width: 22px; height: 22px; margin-right: 10px; flex: none; }

  .brand {
    position: absolute; text-align: center;
    font-weight: 600; color: var(--teal-dark);
  }
  .brand--front { right: 58px; bottom: 42px; width: 270px; }
  .brand__mark {
    display: block; margin: 0 auto 10px; border-radius: 50%;
    background: var(--teal-dark);
  }
  .brand--front .brand__mark { width: 62px; height: 62px; }
  .brand__name { display: block; line-height: 1; }
  .brand--front .brand__name { font-size: 29px; letter-spacing: -0.5px; }
  .brand__tagline { display: block; }
  .brand--front .brand__tagline { font-size: 14px; letter-spacing: 6px; margin-top: 4px; }

  .brand--back {
    left: 0; right: 0; top: 100px; color: var(--teal-raised);
  }
  .brand--back .brand__mark { width: 118px; height: 118px; background: var(--teal-raised); margin-bottom: 22px; }
  .brand--back .brand__name { font-size: 52px; letter-spacing: -1px; }
  .brand--back .brand__tagline { font-size: 24px; letter-spacing: 14px; margin-top: 6px; }
</style>
</head>
<body>
<main class="canvas">

  <section class="card card--front" aria-label="Business card front">
    <header class="holder">
      <h1 class="holder__name">Delia Norwood</h1>
      <p class="holder__role">Owner</p>
    </header>

    <ul class="contact-list">
      <li class="contact-list__item">
        <svg class="contact-list__icon" viewBox="0 0 22 22" aria-hidden="true">
          <circle cx="11" cy="11" r="11" fill="var(--teal-dark)"/>
          <path d="M7.2 5.8l1.9-.4 1.2 2.8-1.3 1c.6 1.4 1.6 2.5 3 3.2l1-1.3 2.8 1.2-.4 1.9c-.2.6-.8 1-1.4.9-4.2-.5-7.2-3.6-7.7-7.8-.1-.6.3-1.2.9-1.5z" fill="#fff"/>
        </svg>
        0473 958 162
      </li>
      <li class="contact-list__item">
        <svg class="contact-list__icon" viewBox="0 0 22 22" aria-hidden="true">
          <circle cx="11" cy="11" r="11" fill="var(--teal-dark)"/>
          <path d="M11 4.5c-2.6 0-4.5 2-4.5 4.4 0 3.2 4.5 8.3 4.5 8.3s4.5-5.1 4.5-8.3c0-2.4-1.9-4.4-4.5-4.4zm0 6.3a1.9 1.9 0 110-3.8 1.9 1.9 0 010 3.8z" fill="#fff"/>
        </svg>
        PO Box 8617 Mossvale NSW 2389
      </li>
      <li class="contact-list__item">
        <svg class="contact-list__icon" viewBox="0 0 22 22" aria-hidden="true">
          <circle cx="11" cy="11" r="11" fill="var(--teal-dark)"/>
          <rect x="5.5" y="7" width="11" height="8" rx="1" fill="#fff"/>
          <path d="M5.8 7.5L11 11.5l5.2-4" fill="none" stroke="var(--teal-dark)" stroke-width="1.2"/>
        </svg>
        info@steadyharbourfinancialservices.com.au
      </li>
      <li class="contact-list__item">
        <svg class="contact-list__icon" viewBox="0 0 22 22" aria-hidden="true">
          <circle cx="11" cy="11" r="11" fill="var(--teal-dark)"/>
          <g fill="none" stroke="#fff" stroke-width="1.2">
            <circle cx="11" cy="11" r="5.5"/>
            <ellipse cx="11" cy="11" rx="2.3" ry="5.5"/>
            <path d="M5.5 11h11"/>
          </g>
        </svg>
        www.steadyharbourfinancialservices.com.au
      </li>
    </ul>

    <div class="brand brand--front">
      <span class="brand__mark" aria-hidden="true"></span>
      <span class="brand__name">STEADY HARBOUR</span>
      <span class="brand__tagline">Financial Services</span>
    </div>
  </section>

  <section class="card card--back" aria-label="Business card back">
    <div class="brand brand--back">
      <span class="brand__mark" aria-hidden="true"></span>
      <span class="brand__name">STEADY HARBOUR</span>
      <span class="brand__tagline">Financial Services</span>
    </div>
  </section>

</main>
</body>
</html>
```